Eavestone screen porch

Can you please design a flyer for me promoting my screen porch businessPlease remove the seamless gutters word from the title and add “screen porches” I have added the logo and a bunch of pictures from projects that I have done in the past. You can use words like Hillcrest Screen porches, etc

Target Market(s)

homeowners, contractors, builders

Industry/Entity Type

Construction

Requirements
Must have
• Dov Kerring
• Eavestone Gutters
• 2937 Old Hwy 52 N, Marlow, TN 37110
• 615-307-6184
Nice to have
• A few colors maybe 3 most
• nice looking font

```html
<!DOCTYPE html>
<html lang="en">
<head>
<meta charset="utf-8">
<title>Hillcrest Screen Porches – Eavestone Gutters</title>
<link rel="stylesheet" href="https://fonts.googleapis.com/css2?family=Montserrat:wght@200;400;500;600;700;800;900&display=swap">
<style>
  :root {
    --red: #e11f2e;
    --red-deep: #a8121c;
    --maroon: #5a0a0f;
    --ink: #1c1c1c;
    --white: #ffffff;
    --photo-light: #8a8780;
    --photo-mid: #4a4a4b;
    --photo-dark: #2b2b2d;
  }
  * { margin: 0; padding: 0; box-sizing: border-box; }
  html, body { width: 777px; height: 1200px; overflow: hidden; background: var(--white); }
  .flyer {
    position: relative;
    width: 777px;
    height: 1200px;
    overflow: hidden;
    font-family: "Montserrat", sans-serif;
    background: var(--white);
  }
  .backdrop { position: absolute; inset: 0; }
  .brand {
    position: absolute;
    left: 40px;
    top: 46px;
    display: flex;
    align-items: center;
    gap: 12px;
  }
  .brand-mark { width: 34px; height: 34px; background: var(--red); flex: none; }
  .brand-name {
    font-size: 30px;
    font-weight: 800;
    color: var(--ink);
    letter-spacing: 1px;
    line-height: 1.05;
    text-transform: uppercase;
  }
  .brand-name span { display: block; }
  .offer {
    position: absolute;
    right: 30px;
    top: 52px;
    text-align: right;
    line-height: 1;
  }
  .offer-title { font-size: 40px; color: var(--red); font-weight: 500; letter-spacing: 0.5px; }
  .offer-title strong { font-weight: 800; }
  .offer-sub { margin-top: 6px; font-size: 21px; font-weight: 600; color: var(--ink); }
  .headline {
    position: absolute;
    left: 50px;
    top: 548px;
    color: var(--white);
    line-height: 1;
    text-shadow: 5px 5px 0 var(--red-deep);
  }
  .headline-region { display: block; font-size: 86px; font-weight: 200; letter-spacing: 1px; text-shadow: none; }
  .headline-main { display: block; font-size: 114px; font-weight: 900; letter-spacing: 1px; margin-top: 19px; }
  .headline-main + .headline-main { margin-top: -4px; }
  .benefits {
    position: absolute;
    right: 30px;
    top: 904px;
    list-style: none;
    text-align: right;
    color: var(--white);
    font-size: 18px;
    font-weight: 500;
    line-height: 27.5px;
  }
  .contact {
    position: absolute;
    left: 42px;
    top: 1036px;
    color: var(--white);
  }
  .contact-name { font-size: 56px; font-weight: 500; color: var(--red); line-height: 1; }
  .contact-address { margin-top: 16px; font-size: 17px; font-weight: 500; }
  .contact-address strong { font-weight: 800; }
  .contact-line { margin-top: 10px; font-size: 23px; font-weight: 800; }
  .contact-line .divider { font-weight: 400; margin: 0 6px; }
  .contact-line .web { color: var(--red); }
</style>
</head>
<body>
<main class="flyer">
  <svg class="backdrop" width="777" height="1200" viewBox="0 0 777 1200">
    <defs>
      <linearGradient id="photoTone" x1="0" y1="0" x2="0" y2="1">
        <stop offset="0" stop-color="#8a8780"/>
        <stop offset="0.3" stop-color="#4a4a4b"/>
        <stop offset="0.7" stop-color="#2b2b2d"/>
        <stop offset="1" stop-color="#7a0d14"/>
      </linearGradient>
    </defs>
    <polygon class="red-field" points="0,246 777,149 777,1200 0,1200" fill="#e11f2e"/>
    <polygon class="project-photo" role="img" aria-label="Photo of a finished screened porch with gabled roof and cable railing deck"
             points="0,276 777,182 777,874 0,1017" fill="url(#photoTone)"/>
    <rect class="footer-band" x="0" y="1017" width="777" height="183" fill="#5a0a0f"/>
    <polygon class="benefit-wedge" points="298,975 777,874 777,1072" fill="#e11f2e"/>
  </svg>

  <div class="brand">
    <span class="brand-mark"></span>
    <p class="brand-name"><span>Eavestone</span><span>Gutters</span></p>
  </div>

  <div class="offer">
    <p class="offer-title"><strong>FREE</strong> ESTIMATES</p>
    <p class="offer-sub">Call us today to start your project!</p>
  </div>

  <h1 class="headline">
    <span class="headline-region">HILLCREST</span>
    <span class="headline-main">SCREEN</span>
    <span class="headline-main">PORCHES</span>
  </h1>

  <ul class="benefits">
    <li>Privacy</li>
    <li>Year-Round Use</li>
    <li>Extend Your Living Space</li>
    <li>New Family Space</li>
    <li>Home Value</li>
    <li>No Bugs</li>
  </ul>

  <div class="contact">
    <p class="contact-name">Dov Kerring</p>
    <p class="contact-address"><strong>EAVESTONE GUTTERS</strong>, 2937 Old Hwy 52 N, Marlow, TN 37110</p>
    <p class="contact-line"><span class="phone">615-307-6184</span><span class="divider">|</span><span class="web">www.eavestonegutterworks.com</span></p>
  </div>
</main>
</body>
</html>
```